Lucid Haven - Need Stationary Design

We need a stationary pack for our new Care company based in the uk
Are corporate colours are Pink and purple
Please use attached logo
Target Market(s)
The Care Industry
Industry/Entity Type
It Company
Contact Information for Business Card
Moira Blythe
Director

```html
<!DOCTYPE html>
<html lang="en">
<head>
<meta charset="utf-8">
<title>Lucid Haven – Stationery</title>
<link href="https://fonts.googleapis.com/css2?family=Arimo:wght@400;700&display=swap" rel="stylesheet">
<style>
  :root {
    --purple: #845ca6;
    --purple-dark: #6f4a93;
    --pink: #e0418f;
    --ink: #3a3a3a;
    --paper: #ffffff;
    --paper-shade: #f3f3f3;
    --backdrop: #e6e3e8;
  }
  * { box-sizing: border-box; margin: 0; padding: 0; }
  html, body { width: 1200px; height: 1000px; overflow: hidden; }
  body {
    position: relative;
    background: var(--backdrop);
    font-family: "Arimo", Arial, sans-serif;
    color: var(--ink);
  }
  .sheet {
    position: absolute;
    background: radial-gradient(ellipse at 55% 45%, var(--paper) 55%, var(--paper-shade) 100%);
    box-shadow: 0 2px 6px rgba(0,0,0,.18);
    overflow: hidden;
  }
  .sheet--purple { background: var(--purple); }
  .wordmark {
    position: absolute;
    font-weight: 700;
    color: var(--purple);
    white-space: nowrap;
    display: flex;
    align-items: center;
    gap: 6px;
  }
  .wordmark__dot {
    display: inline-block;
    border-radius: 50%;
    background: var(--pink);
  }
  .sheet--purple .wordmark { color: var(--paper); }
  .sheet--purple .wordmark__dot { background: var(--paper); }
  .footer-band {
    position: absolute; left: 0; right: 0; bottom: 0;
    background: var(--purple);
    border-top: 3px solid var(--pink);
  }
  .contact { position: absolute; text-align: center; line-height: 1.25; }
  .contact .label { color: var(--purple); }
  .contact .sep { color: var(--pink); }
  .person__name { color: var(--purple); font-weight: 700; }
  .person__role { color: var(--pink); }
  .web { position: absolute; left: 0; right: 0; text-align: center; color: var(--paper); letter-spacing: 1px; }

  /* Letterhead */
  .letterhead { left: 18px; top: 203px; width: 549px; height: 709px; }
  .letterhead .wordmark { left: 26px; top: 92px; font-size: 22px; }
  .letterhead .contact { left: 0; right: 0; top: 664px; font-size: 10px; }
  .letterhead .footer-band { height: 12px; }

  /* Business card horizontal */
  .card-h-front { left: 615px; top: 67px; width: 225px; height: 128px; }
  .card-h-front .wordmark { left: 12px; top: 56px; font-size: 12px; }
  .card-h-front .person { position: absolute; right: 10px; top: 14px; text-align: right; font-size: 9px; line-height: 1.3; }
  .card-h-front .person__role { font-size: 7px; }
  .card-h-front .contact { left: 0; right: 0; top: 88px; font-size: 7px; }
  .card-h-front .footer-band { height: 8px; }
  .card-h-back { left: 615px; top: 207px; width: 225px; height: 129px; }
  .card-h-back .wordmark { left: 0; right: 0; justify-content: center; top: 76px; font-size: 13px; }
  .card-h-back .web { top: 106px; font-size: 7px; }

  /* Business card vertical */
  .card-v-front { left: 857px; top: 111px; width: 130px; height: 225px; }
  .card-v-front .wordmark { left: 0; right: 0; justify-content: center; top: 60px; font-size: 12px; }
  .card-v-front .person { position: absolute; left: 0; right: 0; top: 106px; text-align: center; font-size: 9px; line-height: 1.3; }
  .card-v-front .person__role { font-size: 7px; }
  .card-v-front .contact { left: 0; right: 0; top: 150px; font-size: 7px; }
  .card-v-front .contact--lines { top: 184px; }
  .card-v-front .footer-band { height: 8px; }
  .card-v-back { left: 1003px; top: 111px; width: 128px; height: 225px; }
  .card-v-back .wordmark { left: 0; right: 0; justify-content: center; top: 118px; font-size: 12px; }
  .card-v-back .web { top: 196px; font-size: 7px; letter-spacing: 0; }

  /* Envelope */
  .envelope-front { left: 577px; top: 353px; width: 596px; height: 267px; }
  .envelope-front .wordmark { left: 24px; top: 92px; font-size: 22px; }
  .envelope-front .contact { left: 140px; right: 0; top: 222px; font-size: 10px; }
  .envelope-front .footer-band { height: 12px; }
  .envelope-back { left: 577px; top: 638px; width: 596px; height: 274px; }
  .envelope-back .flap { position: absolute; left: 0; top: 0; }
  .envelope-back .web { top: 49px; font-size: 10px; letter-spacing: 1.5px; }
</style>
</head>
<body>

<section class="sheet letterhead" aria-label="Letterhead">
  <div class="wordmark"><span class="wordmark__dot" style="width:12px;height:12px"></span>Lucid Haven</div>
  <div class="contact">
    <div>42 Meadowbank Road Harrowfield, Ny 12580 <span class="sep">|</span> <span class="label">T:</span> 091-040-55501234</div>
    <div><span class="label">E:</span> info@lucidhaven.com <span class="sep">|</span> <span class="label">W:</span> www.lucidhaven.com</div>
  </div>
  <div class="footer-band"></div>
</section>

<section class="sheet card-h-front" aria-label="Business card front, landscape">
  <div class="wordmark"><span class="wordmark__dot" style="width:7px;height:7px"></span>Lucid Haven</div>
  <div class="person">
    <div class="person__name">Moira Blythe</div>
    <div class="person__role">Managing Director</div>
  </div>
  <div class="contact">
    <div>42 Meadowbank Road Harrowfield, Ny 12580</div>
    <div>T: 091-040-55501234</div>
    <div><span class="label">E:</span> info@lucidhaven.com</div>
  </div>
  <div class="footer-band"></div>
</section>

<section class="sheet sheet--purple card-h-back" aria-label="Business card back, landscape">
  <div class="wordmark"><span class="wordmark__dot" style="width:7px;height:7px"></span>Lucid Haven</div>
  <div class="web">www.lucidhaven.com</div>
</section>

<section class="sheet card-v-front" aria-label="Business card front, portrait">
  <div class="wordmark"><span class="wordmark__dot" style="width:7px;height:7px"></span>Lucid Haven</div>
  <div class="person">
    <div class="person__name">Moira Blythe</div>
    <div class="person__role">Managing Director</div>
  </div>
  <div class="contact">
    <div>42 Meadowbank Road,</div>
    <div>Harrowfield, Ny 12580</div>
    <div>T: 091-040-55501234</div>
  </div>
  <div class="contact contact--lines">
    <div><span class="label">E:</span> info@lucidhaven.com</div>
    <div><span class="label">W:</span> www.lucidhaven.com</div>
  </div>
  <div class="footer-band"></div>
</section>

<section class="sheet sheet--purple card-v-back" aria-label="Business card back, portrait">
  <div class="wordmark"><span class="wordmark__dot" style="width:7px;height:7px"></span>Lucid Haven</div>
  <div class="web">www.lucidhaven.com</div>
</section>

<section class="sheet envelope-front" aria-label="Envelope front">
  <div class="wordmark"><span class="wordmark__dot" style="width:12px;height:12px"></span>Lucid Haven</div>
  <div class="contact">
    <div>42 Meadowbank Road Harrowfield, Ny 12580 <span class="sep">|</span> <span class="label">T:</span> 091-040-55501234</div>
    <div><span class="label">E:</span> info@lucidhaven.com <span class="sep">|</span> <span class="label">W:</span> www.lucidhaven.com</div>
  </div>
  <div class="footer-band"></div>
</section>

<section class="sheet envelope-back" aria-label="Envelope back">
  <svg class="flap" width="596" height="140" viewBox="0 0 596 140" aria-hidden="true">
    <path d="M0 0 H596 V42 Q596 52 584 56 L318 124 Q298 130 278 124 L12 56 Q0 52 0 42 Z" fill="var(--purple)"/>
  </svg>
  <div class="web">www.lucidhaven.com</div>
</section>

</body>
</html>
```